Wool Product Label / Yarn Band

Looking to update the packaging on our wool products. This includes a design for a paper band to place around braided wool or yarn, and a design for a sticker to place on the outside of tissue paper wrapping. Open to updating or modifying the logo, which does not fit well on a round sticker, but the sticker could also be something wool related (like a sheep or drop spindle) that does not include the logo.
Target Market(s)
Wool crafters (knitters / spinners / felters). Mainly women, aged 30-70
Industry/Entity Type
Textile
Colors
Designer to choose colors to be used in the design.
Requirements
Must have
- Band needs to include, brand name, logo, url (fernloomstead.com), dyelot number, as well as the fiber content (ex: Merino Wool) and weight of the fiber (ex: 4oz).
Nice to have
- Band would ideally be easily customized because the weight and fiber content is variable and will be printed specifically for each product, Variable information can be on a sticker or printed directly on a band that can be printed on a standard printer. Attached is a photo of the current band and it's application.

```html
<!DOCTYPE html>
<html lang="en">
<head>
<meta charset="utf-8">
<title>Fernloomstead – Yarn Bands &amp; Sticker</title>
<link rel="stylesheet" href="https://fonts.googleapis.com/css2?family=Montserrat:wght@400;500;600;800&display=swap">
<style>
  :root {
    --leaf: #7cbf2a;
    --leaf-soft: #a5cd55;
    --pattern-tint: #eef6e0;
    --ink: #1a1a1a;
    --paper: #ffffff;
    --edge: #e4e4e4;
  }
  * { box-sizing: border-box; margin: 0; padding: 0; }
  html, body { width: 927px; height: 1200px; overflow: hidden; background: var(--paper); }
  body { position: relative; font-family: "Montserrat", sans-serif; color: var(--ink); }

  .yarn-band {
    position: absolute; left: 76px; width: 789px; height: 297px;
    border: 1px solid var(--edge); border-bottom: none; overflow: hidden; background: var(--paper);
  }
  .yarn-band--solid { top: 50px; }
  .yarn-band--bright { top: 385px; }
  .yarn-band--muted { top: 725px; }

  .wave-field {
    position: absolute; top: 5px; height: 238px; width: 221px;
    background: linear-gradient(180deg, var(--pattern-tint), #e3f0cc);
  }
  .wave-field--left { left: 0; }
  .wave-field--right { right: 0; width: 218px; }

  .band-foot { position: absolute; left: 0; top: 238px; width: 789px; height: 59px; display: block; }

  .brand-mark {
    position: absolute; left: 50%; top: 24px; transform: translateX(-50%);
    width: 58px; height: 58px; border-radius: 50%; background: var(--leaf);
  }
  .brand-name {
    position: absolute; left: 0; right: 0; top: 88px; text-align: center;
    font-weight: 600; font-size: 38px; color: var(--leaf); letter-spacing: 0.5px; line-height: 44px;
  }
  .tagline {
    position: absolute; left: 0; right: 0; top: 141px; text-align: center;
    font-size: 10px; font-weight: 500; letter-spacing: 3px; line-height: 12px;
  }
  .fiber {
    position: absolute; left: 0; right: 0; top: 178px; text-align: center;
    font-size: 14.5px; font-weight: 800; line-height: 18px;
  }
  .fiber::before, .fiber::after {
    content: ""; display: inline-block; width: 6px; height: 6px; border-radius: 50%;
    background: var(--leaf); vertical-align: middle; margin: 0 12px 3px;
  }
  .details {
    position: absolute; left: 0; right: 0; top: 210px; text-align: center;
    font-size: 10.5px; font-weight: 500; line-height: 14px;
  }
  .details .sep { color: var(--leaf); margin: 0 10px; }
  .site {
    position: absolute; left: 0; right: 0; top: 273px; text-align: center;
    font-size: 9.5px; letter-spacing: 3px; color: var(--paper); font-weight: 400;
  }
  .yarn-band--bright .site, .yarn-band--muted .site { font-weight: 500; }

  .lockup { position: absolute; left: 325px; top: 1090px; width: 345px; height: 70px; }
  .lockup .brand-mark { left: 10px; top: 2px; transform: none; width: 62px; height: 62px; }
  .lockup .brand-name {
    left: 108px; right: auto; top: 10px; font-size: 30px; line-height: 36px; text-align: left;
  }
  .lockup .tagline { left: 137px; right: auto; top: 52px; font-size: 8px; letter-spacing: 2.4px; text-align: left; }

  .round-sticker {
    position: absolute; left: 120px; top: 1058px; width: 132px; height: 132px; border-radius: 50%;
    border: 3px solid var(--leaf); background: var(--paper);
    display: flex; flex-direction: column; align-items: center; justify-content: center; gap: 5px;
  }
  .round-sticker .dot { width: 24px; height: 24px; border-radius: 50%; background: var(--leaf); }
  .round-sticker .sticker-name { font-size: 13px; font-weight: 600; color: var(--leaf); line-height: 16px; }
  .round-sticker .sticker-line { font-size: 6px; font-weight: 500; letter-spacing: 1.5px; line-height: 8px; }
</style>
</head>
<body>

<section class="yarn-band yarn-band--solid">
  <div class="wave-field wave-field--left" role="img" aria-label="Fine horizontal wavy green line pattern"></div>
  <div class="wave-field wave-field--right" role="img" aria-label="Fine horizontal wavy green line pattern"></div>
  <svg class="band-foot" viewBox="0 0 789 59" preserveAspectRatio="none" aria-hidden="true">
    <path fill="#a5cd55" d="M0,10 C30,10 30,2 60,2 S90,10 120,10 S150,2 180,2 S210,10 240,10 S270,2 300,2 S330,10 360,10 S390,2 420,2 S450,10 480,10 S510,2 540,2 S570,10 600,10 S630,2 660,2 S690,10 720,10 S750,2 780,2 S810,10 840,10 V59 H0 Z"/>
  </svg>
  <div class="brand-mark"></div>
  <div class="brand-name">Fernloomstead</div>
  <p class="tagline">HAND PAINTED YARN &amp; FIBERS</p>
  <p class="fiber">MERINO WOOL</p>
  <p class="details">Qty: 4.0 oz<span class="sep">•</span>Dye Lot: 0417</p>
  <p class="site">www.fernloomstead.com</p>
</section>

<section class="yarn-band yarn-band--bright">
  <div class="wave-field wave-field--left" role="img" aria-label="Fine horizontal wavy green line pattern"></div>
  <div class="wave-field wave-field--right" role="img" aria-label="Fine horizontal wavy green line pattern"></div>
  <svg class="band-foot" viewBox="0 0 789 59" preserveAspectRatio="none" aria-hidden="true">
    <defs>
      <linearGradient id="spectrum" gradientUnits="userSpaceOnUse" x1="0" y1="0" x2="789" y2="0">
        <stop offset="0" stop-color="#e4521b"/>
        <stop offset="0.3" stop-color="#fdea00"/>
        <stop offset="0.5" stop-color="#a6c91e"/>
        <stop offset="0.72" stop-color="#45a834"/>
        <stop offset="0.88" stop-color="#3a716f"/>
        <stop offset="1" stop-color="#6c3582"/>
      </linearGradient>
    </defs>
    <path fill="none" stroke="url(#spectrum)" stroke-width="2" d="M0,10 C30,10 30,2 60,2 S90,10 120,10 S150,2 180,2 S210,10 240,10 S270,2 300,2 S330,10 360,10 S390,2 420,2 S450,10 480,10 S510,2 540,2 S570,10 600,10 S630,2 660,2 S690,10 720,10 S750,2 780,2 S810,10 840,10" transform="translate(0,2)"/>
    <path fill="url(#spectrum)" d="M0,10 C30,10 30,2 60,2 S90,10 120,10 S150,2 180,2 S210,10 240,10 S270,2 300,2 S330,10 360,10 S390,2 420,2 S450,10 480,10 S510,2 540,2 S570,10 600,10 S630,2 660,2 S690,10 720,10 S750,2 780,2 S810,10 840,10 V51 H0 Z" transform="translate(0,8)"/>
  </svg>
  <div class="brand-mark"></div>
  <div class="brand-name">Fernloomstead</div>
  <p class="tagline">HAND PAINTED YARN &amp; FIBERS</p>
  <p class="fiber">MERINO WOOL/ BAMBOO/ SILK ROVING</p>
  <p class="details">Qty: 4.0 oz<span class="sep">•</span>Dye Lot: 0418</p>
  <p class="site">www.fernloomstead.com</p>
</section>

<section class="yarn-band yarn-band--muted">
  <div class="wave-field wave-field--left" role="img" aria-label="Fine horizontal wavy green line pattern"></div>
  <div class="wave-field wave-field--right" role="img" aria-label="Fine horizontal wavy green line pattern"></div>
  <svg class="band-foot" viewBox="0 0 789 59" preserveAspectRatio="none" aria-hidden="true">
    <defs>
      <linearGradient id="heather" gradientUnits="userSpaceOnUse" x1="0" y1="0" x2="789" y2="0">
        <stop offset="0" stop-color="#cd7a4b"/>
        <stop offset="0.2" stop-color="#dca850"/>
        <stop offset="0.45" stop-color="#b5b55c"/>
        <stop offset="0.65" stop-color="#7fa35e"/>
        <stop offset="0.82" stop-color="#5a7588"/>
        <stop offset="1" stop-color="#6e6aa6"/>
      </linearGradient>
      <linearGradient id="heather-line" gradientUnits="userSpaceOnUse" x1="0" y1="0" x2="789" y2="0">
        <stop offset="0" stop-color="#c2501a"/>
        <stop offset="0.3" stop-color="#c9a12c"/>
        <stop offset="0.6" stop-color="#5c8d3c"/>
        <stop offset="1" stop-color="#2d4d8c"/>
      </linearGradient>
    </defs>
    <path fill="none" stroke="url(#heather-line)" stroke-width="2" d="M0,10 C30,10 30,2 60,2 S90,10 120,10 S150,2 180,2 S210,10 240,10 S270,2 300,2 S330,10 360,10 S390,2 420,2 S450,10 480,10 S510,2 540,2 S570,10 600,10 S630,2 660,2 S690,10 720,10 S750,2 780,2 S810,10 840,10" transform="translate(0,2)"/>
    <path fill="url(#heather)" d="M0,10 C30,10 30,2 60,2 S90,10 120,10 S150,2 180,2 S210,10 240,10 S270,2 300,2 S330,10 360,10 S390,2 420,2 S450,10 480,10 S510,2 540,2 S570,10 600,10 S630,2 660,2 S690,10 720,10 S750,2 780,2 S810,10 840,10 V51 H0 Z" transform="translate(0,8)"/>
  </svg>
  <div class="brand-mark"></div>
  <div class="brand-name">Fernloomstead</div>
  <p class="tagline">HAND PAINTED YARN &amp; FIBERS</p>
  <p class="fiber">MERINO WOOL/ BAMBOO/ SILK ROVING</p>
  <p class="details">Qty: 4.0 oz<span class="sep">•</span>Dye Lot: 0419</p>
  <p class="site">www.fernloomstead.com</p>
</section>

<section class="round-sticker">
  <div class="dot"></div>
  <p class="sticker-name">Fernloomstead</p>
  <p class="sticker-line">HAND PAINTED</p>
  <p class="sticker-line">fernloomstead.com</p>
</section>

<section class="lockup">
  <div class="brand-mark"></div>
  <div class="brand-name">Fernloomstead</div>
  <p class="tagline">HAND PAINTED YARN &amp; FIBERS</p>
</section>

</body>
</html>
```